Healthy Lifestyle Vitamin Supplement Company needs a web site designed.

We are starting a new website for selling quality natural vitamins and supplements online plus providing news and information on healthy living. We DO NOT need any programming done for this site. Just the design in a layered photoshop file. This site needs to communicate that we are the authoritative source for healthy living and a trusted place to buy supplements and information on living a healthy lifestyle.

Triggers On page will be

Trigger set 1
Home - Shop By Brand - Top Sellers - Clearance - Help Center - My Favorites

Trigger set 2
Vitamins and Herbs - Natural Living - Aromatherapy - Coffee and Tea - Health and Beauty - Healthy Foods - Pet Health - Sports and Diet

Triggers Other
Login - Shopping Cart - Checkout - Track Order

Need a search bar in the design

Left side should be categories look at Brelvox.com for example of categories.

Name and domain name is Sunward Meadow Crest

Will also need a logo to go along with that.

Industry/Entity Type

It Company

```html
<!DOCTYPE html>
<html lang="en">
<head>
<meta charset="utf-8">
<title>Sunward Meadow Crest</title>
<link href="https://fonts.googleapis.com/css2?family=Roboto:wght@300;400;500;700&display=swap" rel="stylesheet">
<style>
:root{
  --green:#4cb286;
  --green-dark:#138a4a;
  --green-light:#d9efe5;
  --ink:#333;
  --muted:#555;
  --pink:#e0457b;
  --red:#d9243a;
  --topbar:#262626;
  --gray-bg:#f3f3f3;
  --line:#ddd;
}
*{box-sizing:border-box;margin:0;padding:0}
html,body{width:735px;height:1200px;overflow:hidden}
body{position:relative;background:#fff;font-family:'Roboto',Arial,sans-serif;color:var(--ink)}
.abs{position:absolute}

.topbar{left:0;top:0;width:735px;height:25px;background:var(--topbar);color:#fff;font-size:7.5px}
.topbar .sel{top:6px;height:13px;background:#3a3a3a;border-radius:2px;padding:2px 5px;font-size:6.5px}
.topbar .cart{left:410px;top:8px}
.topbar .links{left:507px;top:8px;word-spacing:1px}

.logo{left:54px;top:46px;font-size:17px;font-weight:500;letter-spacing:.2px;color:var(--ink)}
.logo b{color:var(--green);font-weight:500}
.search{left:552px;top:26px;width:130px;height:22px;border:1px solid var(--line);font-size:7px;color:#888;padding:6px 7px}
.search .btn{position:absolute;right:-1px;top:-1px;width:25px;height:22px;background:var(--green)}
.mainnav{top:58px;right:54px;display:flex;gap:15px;font-size:7px;color:var(--ink)}
.mainnav .on{color:var(--green)}

.catbar{left:54px;top:84px;width:628px;height:35px;background:linear-gradient(#63c297,#4cb286);border-radius:2px;display:flex;justify-content:space-between;align-items:center;padding:0 11px;color:#fff;font-size:6.8px}

.hero{left:54px;top:124px;width:628px;height:294px;border:1px solid var(--line);padding:3px;box-shadow:0 8px 10px -6px rgba(0,0,0,.35)}
.hero .photo{width:100%;height:100%;background:linear-gradient(90deg,#dfe8da 0%,#f2f4f1 55%,#e8ebe8 100%)}
.hero .shots{left:4px;top:4px;width:340px;height:286px;background:radial-gradient(ellipse at 50% 55%,#1f5a2f 0%,#9cc58a 55%,#e6ece2 80%)}
.hero h2{left:352px;top:98px;font-size:21px;font-weight:400;color:#444}
.hero h2 b{color:var(--green);font-weight:400}
.hero p{left:354px;top:132px;width:230px;font-size:12px;line-height:20px;color:#444;font-weight:300}
.hero .buy{left:353px;top:182px;width:107px;height:35px;background:var(--green-dark);color:#fff;font-size:13.5px;padding:8px 11px;display:flex;align-items:center;gap:8px}
.dots{left:284px;top:270px;display:flex;gap:5px}
.dots i{width:7px;height:7px;border-radius:50%;background:#fff;border:1px solid #ccc}
.dots i.on{background:var(--green)}

.promo{top:433px;width:312px;height:148px;border:1px solid var(--line);padding:3px}
.promo .in{position:relative;width:100%;height:100%;background:linear-gradient(180deg,#dff1e8,#c3e4d4)}
.promo .pic{position:absolute}
.sale .big{left:26px;top:44px;font-size:31px;font-weight:500;color:var(--green);line-height:1}
.sale .small{left:26px;top:80px;font-size:6px;color:#222}
.sale .off{left:26px;top:91px;font-size:19px;color:var(--red)}
.aroma .t1{left:23px;top:45px;font-size:15px;font-weight:500;color:var(--green)}
.aroma .t2{left:23px;top:65px;font-size:8px;color:#222}
.aroma .t3{left:23px;top:84px;font-size:15px;font-weight:500;color:var(--red)}

.shop{left:0;top:609px;width:735px;height:455px;background:var(--gray-bg);border-top:1px solid #e2e2e2}
.cats{left:54px;top:13px;width:171px;height:426px;background:#fff;box-shadow:0 0 4px rgba(0,0,0,.15)}
.cats h3{height:28px;background:var(--green);color:#fff;font-size:10px;font-weight:400;padding:9px 19px;position:relative}
.cats h3 .arr{position:absolute;right:13px;top:7px}
.cats ul{list-style:none;padding:0 11px}
.cats li{height:30.4px;border-bottom:1px dotted #777;font-size:8px;padding:14px 11px 0;color:#222}
.cats li:last-child{border:0}
.feat{left:240px;top:18px;width:414px;font-size:12px;font-weight:500;color:#222;border-bottom:1px solid #ccc;padding-bottom:7px}
.card{width:136px;height:194px;background:#fff;border:1px solid #d5d5d5}
.card .img{position:absolute;left:8px;top:8px;width:118px;height:120px;border:1px solid #ddd;background:radial-gradient(circle,#fff 40%,#e7e7e7 100%);display:flex;align-items:center;justify-content:center}
.card .img span{width:44px;height:80px;border-radius:8px}
.card .nm{position:absolute;top:136px;width:100%;text-align:center;font-size:7px;color:#222}
.card .pr{position:absolute;top:150px;width:100%;text-align:center;font-size:9px;color:var(--pink)}
.card .add{position:absolute;left:21px;top:165px;width:92px;height:21px;background:var(--green);border-radius:2px;color:#fff;font-size:6.8px;display:flex;align-items:center;justify-content:center;gap:6px;box-shadow:0 2px 2px rgba(0,0,0,.2)}

.footer{left:0;top:1064px;width:735px;height:118px;background:var(--green);color:#fff}
.fcol{top:21px;font-size:8px}
.fcol h4{font-weight:400;font-size:8.5px;margin-bottom:9px}
.fcol li{list-style:none;font-size:6.5px;margin-bottom:7px;padding-left:9px;position:relative}
.fcol li::before{content:"";position:absolute;left:0;top:2px;width:3.5px;height:3.5px;border-radius:50%;background:#fff}
.pay{left:524px;top:21px;display:flex;gap:4px}
.pay i{width:21px;height:13px;background:#fff;border-radius:1px}
.social{left:524px;top:42px;display:flex;gap:1px}
.social i{width:17px;height:17px;background:#2f7fc1}
.social i:nth-child(3){background:#f0a23a}
.copy{left:527px;top:74px;font-size:9.5px}
.copy small{display:block;font-size:6.3px;margin-top:1px}
.bottom{left:0;top:1182px;width:735px;height:18px;background:#2a2a2a}
</style>
</head>
<body>

<header class="abs topbar">
  <div class="abs sel" style="left:58px">▪ ▾</div>
  <div class="abs sel" style="left:84px">USD ▾</div>
  <div class="abs cart">
    <svg width="11" height="9" viewBox="0 0 11 9" style="vertical-align:-1px"><path d="M0 1h2l2 5h5l1.5-4H3" fill="none" stroke="#4cb286" stroke-width="1.2"/><circle cx="4.5" cy="8" r="1" fill="#4cb286"/><circle cx="8.5" cy="8" r="1" fill="#4cb286"/></svg>
    0 item(s) - $0.00
  </div>
  <div class="abs links">Login &nbsp;|&nbsp; Shopping Cart &nbsp;|&nbsp; Checkout &nbsp;|&nbsp; Track Order</div>
</header>

<div class="abs logo"><b>SUNWARD</b> MEADOW CREST</div>
<div class="abs search">Search
  <div class="btn"><svg width="25" height="22" viewBox="0 0 25 22"><circle cx="11.5" cy="10" r="4.5" fill="none" stroke="#fff" stroke-width="1.6"/><path d="M15 13.5l3.5 3.5" stroke="#fff" stroke-width="1.8"/></svg></div>
</div>
<nav class="abs mainnav">
  <span class="on">HOME</span><span>SHOP BY BRAND</span><span>TOP SELLERS</span><span>CLEARANCE</span><span>HELP CENTER</span><span>MY FAVORITES</span>
</nav>

<nav class="abs catbar">
  <span>VITAMINS AND HERBS</span><span>NATURAL LIVING</span><span>AROMATHERAPY</span><span>COFFEE AND TEA</span><span>HEALTH AND BEAUTY</span><span>HEALTHY FOODS</span><span>PET HEALTH</span><span>SPORTS AND DIET</span>
</nav>

<section class="abs hero">
  <div class="photo"></div>
  <div class="abs shots" role="img" aria-label="Three green supplement jars under fresh green leaves"></div>
  <h2 class="abs"><b>SUNWARD</b> MEADOW CREST</h2>
  <p class="abs">Lorem Ipsum is simply dummy text of the printing and typesetting industry</p>
  <div class="abs buy">BUY NOW
    <svg width="16" height="16" viewBox="0 0 16 16"><circle cx="8" cy="8" r="7.5" fill="#fff"/><path d="M6.5 4.5L10 8l-3.5 3.5" fill="none" stroke="#138a4a" stroke-width="1.8"/></svg>
  </div>
  <div class="abs dots"><i></i><i class="on"></i><i></i><i></i><i></i></div>
</section>

<section class="abs promo sale" style="left:54px">
  <div class="in">
    <div class="pic" style="left:104px;top:30px;width:180px;height:90px;background:linear-gradient(90deg,#d83b46,#c7364a 30%,#3d3f9a 55%,#2d8a3e 80%,#3b9a4a)" role="img" aria-label="Row of assorted supplement bottles"></div>
    <div class="abs big">SALE</div>
    <div class="abs small">NEQUE PORRO QUISQUAM</div>
    <div class="abs off">30% OFF</div>
  </div>
</section>

<section class="abs promo aroma" style="left:370px">
  <div class="in">
    <div class="pic" style="left:140px;top:14px;width:165px;height:110px;background:radial-gradient(ellipse at 60% 55%,#3f4a2a 0%,#6f9a4e 35%,rgba(200,225,205,0) 75%)" role="img" aria-label="Essential oil bottle with rosemary sprigs and lavender flowers"></div>
    <div class="abs t1">AROMATHERAPY</div>
    <div class="abs t2">NEQUE PORRO QUISQUAM</div>
    <div class="abs t3">SPECIAL OFFER</div>
  </div>
</section>

<section class="abs shop">
  <aside class="abs cats">
    <h3>CATEGORIES
      <svg class="arr" width="13" height="13" viewBox="0 0 13 13"><circle cx="6.5" cy="6.5" r="5.8" fill="none" stroke="#fff" stroke-width="1"/><path d="M5.5 4l2.5 2.5L5.5 9" fill="none" stroke="#fff" stroke-width="1.2"/></svg>
    </h3>
    <ul>
      <li>Product name</li><li>Product name</li><li>Product name</li><li>Product name</li>
      <li>Product name</li><li>Product name</li><li>Product name</li><li>Product name</li>
      <li>Product name</li><li>Product name</li><li>Product name</li><li>Product name</li>
    </ul>
  </aside>

  <h3 class="abs feat">FEATURED PRODUCTS</h3>

  <div class="abs card" style="left:240px;top:42px"><div class="img" role="img" aria-label="Blue protein powder tub"><span style="background:linear-gradient(#1b3f9c,#2a5ec9)"></span></div><div class="nm">PRODUCT NAME</div><div class="pr">$ 529.95</div><div class="add"><svg width="11" height="9" viewBox="0 0 11 9"><path d="M0 1h2l2 5h5l1.5-4H3z" fill="#fff"/><circle cx="4.5" cy="8" r="1" fill="#fff"/><circle cx="8.5" cy="8" r="1" fill="#fff"/></svg>ADD TO CART</div></div>
  <div class="abs card" style="left:386px;top:42px"><div class="img" role="img" aria-label="White supplement bottle with blue label"><span style="background:linear-gradient(#f4f4f4,#cfd9e6 50%,#2e6bb0)"></span></div><div class="nm">PRODUCT NAME</div><div class="pr">$ 609.95</div><div class="add"><svg width="11" height="9" viewBox="0 0 11 9"><path d="M0 1h2l2 5h5l1.5-4H3z" fill="#fff"/><circle cx="4.5" cy="8" r="1" fill="#fff"/><circle cx="8.5" cy="8" r="1" fill="#fff"/></svg>ADD TO CART</div></div>
  <div class="abs card" style="left:532px;top:42px"><div class="img" role="img" aria-label="Green vitamin bottle with yellow cap"><span style="background:linear-gradient(#f3c630 20%,#1f5a2f 22%,#e9e2c6 55%,#1f5a2f)"></span></div><div class="nm">PRODUCT NAME</div><div class="pr">$ 319.95</div><div class="add"><svg width="11" height="9" viewBox="0 0 11 9"><path d="M0 1h2l2 5h5l1.5-4H3z" fill="#fff"/><circle cx="4.5" cy="8" r="1" fill="#fff"/><circle cx="8.5" cy="8" r="1" fill="#fff"/></svg>ADD TO CART</div></div>
  <div class="abs card" style="left:240px;top:246px"><div class="img" role="img" aria-label="Red fish oil bottle"><span style="background:linear-gradient(#c8202f,#e2e2e2 50%,#b01e2c)"></span></div><div class="nm">PRODUCT NAME</div><div class="pr">$ 529.95</div><div class="add"><svg width="11" height="9" viewBox="0 0 11 9"><path d="M0 1h2l2 5h5l1.5-4H3z" fill="#fff"/><circle cx="4.5" cy="8" r="1" fill="#fff"/><circle cx="8.5" cy="8" r="1" fill="#fff"/></svg>ADD TO CART</div></div>
  <div class="abs card" style="left:386px;top:246px"><div class="img" role="img" aria-label="White vitamin bottle with yellow label"><span style="background:linear-gradient(#f5f5f5,#e8d88a 50%,#f1f1f1)"></span></div><div class="nm">PRODUCT NAME</div><div class="pr">$ 609.95</div><div class="add"><svg width="11" height="9" viewBox="0 0 11 9"><path d="M0 1h2l2 5h5l1.5-4H3z" fill="#fff"/><circle cx="4.5" cy="8" r="1" fill="#fff"/><circle cx="8.5" cy="8" r="1" fill="#fff"/></svg>ADD TO CART</div></div>
  <div class="abs card" style="left:532px;top:246px"><div class="img" role="img" aria-label="Dark blue collagen bottle"><span style="background:linear-gradient(#1f2f8a,#4a6fc9 55%,#1f2f8a)"></span></div><div class="nm">PRODUCT NAME</div><div class="pr">$ 319.95</div><div class="add"><svg width="11" height="9" viewBox="0 0 11 9"><path d="M0 1h2l2 5h5l1.5-4H3z" fill="#fff"/><circle cx="4.5" cy="8" r="1" fill="#fff"/><circle cx="8.5" cy="8" r="1" fill="#fff"/></svg>ADD TO CART</div></div>
</section>

<footer class="abs footer">
  <div class="abs fcol" style="left:109px"><h4>IMPORTANT LINKS</h4><ul><li>Affiliate Program</li><li>Special Promotions</li><li>Newsletter</li><li>Contact</li></ul></div>
  <div class="abs fcol" style="left:244px"><h4>SUPPORT MENU</h4><ul><li>Lost Password?</li><li>Your Membership</li><li>Your Account</li><li>Support Forum</li></ul></div>
  <div class="abs fcol" style="left:382px"><h4>ABOUT US</h4><ul><li>Customer focus</li><li>Performance</li><li>Innovation</li><li>Responsibility</li></ul></div>
  <div class="abs pay" aria-label="Accepted payment methods"><i></i><i></i><i></i><i></i></div>
  <div class="abs social" aria-label="Social links"><i></i><i></i><i></i><i></i><i></i></div>
  <div class="abs copy">COPYRIGHT<small>© 2014 &nbsp;PRIVACY POLICY</small></div>
</footer>
<div class="abs bottom"></div>

</body>
</html>
```